Varneck Law Business cards and stationary design project

We are looking for a stationary design for business cards (double sided), 8x10, 5x7, and legal and standard envelopes.

We would like the design to match the logo that we have already.
Color palate preferred is Teal, White, grey and any others that will look good for a professional law firm.

We would like this statement: "RELATIONSHIPS. RESPECT. RESULT" to be on the back of the business cards and maybe on the stationary if it looks good.

Please see link to website for more information: www.varneck-law-example.com

Target Market(s)

Potential clients that need Attorney services.

Industry/Entity Type

Law Firm

Contact Information for Business Card

We would like the front and back to be two different colors. Current business cards are teal front, grey back and are a vertical design. We are open to options with colors.

Font styles to use
Serif

Colors
33a6d7
33b8a4
b9b9b9
5c5c5c

Requirements
Must have
• Logo supplied needs to go on the card and stationary.
• Match website color palate, www.varneck-law-example.com
• Be professional and not too wordy.
• Criminal Law, Civil Litigation, Personal Injury, Restraining Orders need to be on the card.
Nice to have
• RELATIONSHIPS. RESPECT. RESULTS. on the back of the card.
Should not have
• Not be too busy/wordy or too flashy.

```html
<!DOCTYPE html>
<html lang="en">
<head>
<meta charset="utf-8">
<title>Varneck Law – Business Card</title>
<link rel="stylesheet" href="https://fonts.googleapis.com/css2?family=Cinzel:wght@400;600&family=Open+Sans:wght@400;600&display=swap">
<style>
  :root {
    --teal: #33b8a4;
    --teal-deep: #2a9aa0;
    --grey-light: #b9b9b9;
    --grey-mid: #8a8a8a;
    --grey-dark: #5c5c5c;
    --charcoal: #383b3e;
    --ink: #2b2b2b;
    --paper: #ffffff;
    --backdrop: #ecebe8;
  }
  * { margin: 0; padding: 0; box-sizing: border-box; }
  html, body { width: 1200px; height: 800px; overflow: hidden; }
  body {
    background: var(--backdrop);
    display: flex;
    align-items: center;
    justify-content: center;
    gap: 40px;
  }
  .card {
    position: relative;
    width: 560px;
    height: 320px;
    border-radius: 4px;
    box-shadow: 0 6px 20px rgba(0,0,0,0.18);
    overflow: hidden;
  }

  /* Front */
  .card-front { background: var(--paper); }
  .front-brand {
    position: absolute;
    top: 48px; left: 150px;
    text-align: center;
  }
  .brand-name {
    font-family: "Cinzel", serif;
    font-weight: 400;
    font-size: 28px;
    letter-spacing: 3px;
    color: var(--teal-deep);
  }
  .front-brand .brand-rule {
    display: block;
    width: 120px; height: 1px;
    margin: 10px auto 0;
    background: var(--teal);
  }
  .holder {
    position: absolute;
    right: 34px; top: 150px;
    text-align: right;
  }
  .holder-name {
    font-family: "Cinzel", serif;
    font-weight: 600;
    font-size: 22px;
    letter-spacing: 2px;
    color: var(--teal-deep);
  }
  .holder-role {
    font-family: "Open Sans", sans-serif;
    font-weight: 600;
    font-size: 11px;
    letter-spacing: 1px;
    color: var(--ink);
    margin-top: 2px;
  }
  .contact-list {
    list-style: none;
    margin-top: 8px;
    font-family: "Open Sans", sans-serif;
    font-size: 12.5px;
    line-height: 1.55;
    color: var(--ink);
  }
  .contact-list .tag { color: var(--teal-deep); font-weight: 600; margin-left: 6px; }
  .address {
    position: absolute;
    left: 54px; bottom: 34px;
    font-family: "Open Sans", sans-serif;
    font-size: 12px;
    letter-spacing: 0.5px;
    text-transform: uppercase;
    color: var(--teal);
  }
  .address-marker {
    position: absolute;
    left: 28px; bottom: 35px;
    width: 12px; height: 12px;
    background: var(--grey-mid);
  }
  .front-band {
    position: absolute;
    left: 0; right: 0; bottom: 0;
    height: 22px;
  }

  /* Back */
  .card-back { background: var(--charcoal); }
  .back-content {
    position: absolute;
    top: 44px; left: 40px; right: 40px;
  }
  .back-content .brand-name {
    font-size: 40px;
    letter-spacing: 4px;
    color: var(--teal);
  }
  .back-content .brand-rule {
    display: block;
    width: 80px; height: 1px;
    margin: 8px 0 18px 4px;
    background: var(--teal);
  }
  .tagline {
    font-family: "Cinzel", serif;
    font-size: 21px;
    letter-spacing: 1px;
    color: #f2f2f2;
  }
  .tagline-rule {
    height: 2px;
    margin-top: 10px;
    background: var(--teal);
    width: 380px;
  }
  .practice-areas {
    position: absolute;
    right: 34px; bottom: 28px;
    list-style: none;
    text-align: right;
    font-family: "Open Sans", sans-serif;
    font-size: 12.5px;
    line-height: 1.6;
    color: #e6e6e6;
  }
  .practice-areas li::after {
    content: "";
    display: inline-block;
    width: 6px; height: 6px;
    margin-left: 7px;
    border-radius: 50%;
    background: var(--teal);
    vertical-align: middle;
  }
</style>
</head>
<body>
  <section class="card card-front" aria-label="Business card front">
    <div class="front-brand">
      <div class="brand-name">Varneck Law</div>
      <span class="brand-rule"></span>
    </div>

    <div class="holder">
      <div class="holder-name">Claire Varneck</div>
      <div class="holder-role">LAWYER</div>
      <ul class="contact-list">
        <li>(555) 014-2370<span class="tag">[P]</span></li>
        <li>claire@varneck-law-example.com<span class="tag">[E]</span></li>
        <li>www.varneck-law-example.com<span class="tag">[W]</span></li>
      </ul>
    </div>

    <span class="address-marker"></span>
    <div class="address">4150 Harbor View Ave, #210, Bayside, CA 90000</div>

    <svg class="front-band" viewBox="0 0 560 22" preserveAspectRatio="none" aria-hidden="true">
      <rect x="0" y="0" width="560" height="2" fill="#8a8a8a"/>
      <rect x="0" y="6" width="560" height="16" fill="#e4e4e4"/>
    </svg>
  </section>

  <section class="card card-back" aria-label="Business card back">
    <div class="back-content">
      <div class="brand-name">Varneck Law</div>
      <span class="brand-rule"></span>
      <div class="tagline">Relationships. Respect. Results.</div>
      <div class="tagline-rule"></div>
    </div>
    <ul class="practice-areas">
      <li>Practice areas</li>
      <li>Criminal Law</li>
      <li>Restraining Orders</li>
      <li>Civil Litigation/Personal Injury</li>
    </ul>
  </section>
</body>
</html>
```